Need a Facebook image for childcare advertisement

We are after a design for Facebook advertisement for childcare and kindergarten centre enrolments for 2023.

I have attached a previous flyer that we have in pdf format. The new logo is also attached with this brief.

All other information is still current as per the attached flyer.

You can use same colours as per attached flyer. I will also attached some stock images that you can select to use for the design.

our website for your reference:

https://tallowmere-vale.com.au

```html
<!DOCTYPE html>
<html lang="en">
<head>
<meta charset="utf-8">
<title>Tallowmere Vale – Enrolments 2023</title>
<link rel="stylesheet" href="https://fonts.googleapis.com/css2?family=Baloo+2:wght@600;700;800&display=swap">
<style>
  :root {
    --navy: #0b3f84;
    --sky: #5cb3e6;
    --white: #ffffff;
    --cloud: #e9eff5;
    --sun: #f6d93c;
    --photo-a: #e9dcc8;
    --photo-b: #b9d4e8;
    --photo-c: #d84a45;
  }
  html, body {
    margin: 0;
    width: 1200px;
    height: 1200px;
    overflow: hidden;
    background: var(--navy);
  }
  .canvas {
    position: relative;
    width: 1080px;
    height: 1080px;
    transform: scale(calc(1200 / 1080));
    transform-origin: 0 0;
    background: var(--navy);
    font-family: "Baloo 2", "Trebuchet MS", sans-serif;
    overflow: hidden;
  }
  .shapes {
    position: absolute;
    inset: 0;
    width: 1080px;
    height: 1080px;
  }
  .brand {
    position: absolute;
    left: 60px;
    top: 92px;
    display: flex;
    align-items: center;
    gap: 14px;
  }
  .brand-dot {
    width: 38px;
    height: 38px;
    border-radius: 50%;
    background: var(--navy);
  }
  .brand-name {
    font-size: 40px;
    font-weight: 800;
    color: var(--navy);
    line-height: 1;
    letter-spacing: 0.5px;
  }
  .headline {
    position: absolute;
    left: 55px;
    top: 452px;
    margin: 0;
    font-weight: 800;
    line-height: 1;
  }
  .headline-main {
    display: block;
    font-size: 72px;
    line-height: 70px;
    color: var(--sky);
  }
  .headline-sub {
    display: block;
    font-size: 50px;
    line-height: 56px;
    color: var(--white);
    margin-top: 4px;
  }
  .headline-year {
    display: block;
    font-size: 112px;
    line-height: 96px;
    color: var(--white);
  }
  .cta {
    position: absolute;
    left: 55px;
    top: 872px;
    margin: 0;
    font-size: 32px;
    font-weight: 700;
    color: var(--sky);
  }
  .contact {
    position: absolute;
    left: 55px;
    top: 937px;
    margin: 0;
    padding: 0;
    list-style: none;
    font-size: 22px;
    font-weight: 700;
    line-height: 30px;
    color: var(--white);
  }
</style>
</head>
<body>
<main class="canvas">
  <svg class="shapes" viewBox="0 0 1080 1080" aria-hidden="false">
    <defs>
      <clipPath id="photo-clip">
        <circle cx="950" cy="240" r="560"/>
      </clipPath>
      <linearGradient id="photo-tone" x1="0" y1="0" x2="1" y2="1">
        <stop offset="0" stop-color="var(--photo-a)"/>
        <stop offset="0.55" stop-color="var(--photo-b)"/>
        <stop offset="1" stop-color="#9cc6e6"/>
      </linearGradient>
    </defs>

    <g class="photo" role="img" aria-label="Photo of a young boy in a striped shirt drawing with crayons at a classroom table">
      <circle cx="950" cy="240" r="560" fill="url(#photo-tone)"/>
      <g clip-path="url(#photo-clip)">
        <circle class="photo-ring" cx="950" cy="240" r="525" fill="none" stroke="var(--sun)" stroke-width="70" opacity="0.6"/>
      </g>
    </g>

    <path class="cloud-top" fill="var(--white)"
      d="M0 0 H585 C600 60 560 110 505 118 C515 190 440 240 380 212 C345 262 265 258 238 222 C198 252 128 244 108 208 C68 230 22 220 0 204 Z"/>

    <g class="cloud-small" fill="var(--cloud)">
      <path d="M458 100 C458 88 470 82 480 86 C486 70 510 66 520 80 C534 74 548 84 545 96 C556 98 560 104 560 104 H458 Z"/>
      <path d="M462 512 C462 498 476 492 488 497 C496 478 526 474 538 492 C554 484 572 496 568 510 C582 512 598 512 598 512 H462 Z"/>
      <path d="M795 818 C795 802 812 794 826 800 C836 778 872 774 886 796 C904 786 924 800 920 816 C932 818 934 818 934 818 H795 Z"/>
    </g>

    <path class="cloud-bottom" fill="var(--white)"
      d="M545 1080 C560 1040 612 1030 640 1050 C668 1000 742 992 770 1032 C800 980 872 962 920 990 C952 930 1040 912 1080 940 V1080 Z"/>
  </svg>

  <div class="brand">
    <span class="brand-dot"></span>
    <span class="brand-name">Tallowmere Vale</span>
  </div>

  <h1 class="headline">
    <span class="headline-main">Childcare &amp;</span>
    <span class="headline-main">kindergarten</span>
    <span class="headline-main">Centre</span>
    <span class="headline-sub">enrolments for</span>
    <span class="headline-year">2023</span>
  </h1>

  <p class="cta">Contact us to secure your child's spot</p>

  <ul class="contact">
    <li>(03) 9000 4127</li>
    <li>admin@tallowmere-vale.com.au</li>
    <li>https://www.tallowmere-vale.com.au/</li>
  </ul>
</main>
</body>
</html>
```